Bytemill - a software development company requires letter head

I currently have a business card and logo, I just need a nice looking letter head the matches the two. I will upload these Illustrator files.

I would like the letter head to be done in a current version of MS Word.

Please incorporate 'bytemill' as per the attached font and the logo.

Industry/Entity Type

Computer Software

Colors

Designer to choose colors to be used in the design.

Requirements
Must have
• Fits in with current design, sleek and professional. It will be used for quotations and tenders and documentation going to clients and potential clients.
• Would like to company logo up the top header and perhaps a watermark of the logo at the bottom right, a bit like the business card.
• Also it needs to be MS word.
• Please work with the color pallet from the attached files.

```html
<!DOCTYPE html>
<html lang="en">
<head>
<meta charset="utf-8">
<title>Bytemill Letterhead</title>
<link rel="stylesheet" href="https://fonts.googleapis.com/css2?family=PT+Sans:wght@400;700&family=Tinos&display=swap">
<style>
  :root {
    --ink-dark: #4d4d4d;
    --brand-blue: #29abe2;
    --wave-blue: #67c3ea;
    --band-grey: #cccccc;
    --contact-grey: #d4d4d4;
    --divider-grey: #c8c8c8;
    --body-ink: #000000;
    --page: #ffffff;
  }
  * { margin: 0; padding: 0; box-sizing: border-box; }
  html, body { width: 1200px; height: 1000px; overflow: hidden; background: var(--page); }
  .canvas { position: relative; width: 1200px; height: 1000px; }

  .header { position: absolute; left: 198px; top: 60px; width: 724px; height: 140px; }
  .header-band { position: absolute; left: 0; top: 0; width: 724px; height: 123px; background: var(--ink-dark); }
  .header-accent { position: absolute; left: 0; top: 123px; width: 724px; height: 7px; background: var(--brand-blue); }
  .header-rule { position: absolute; left: 0; top: 130px; width: 724px; height: 9px; background: var(--band-grey); }

  .brand-mark { position: absolute; left: 74px; top: 16px; width: 56px; height: 56px; border-radius: 50%; background: var(--brand-blue); }
  .brand-name {
    position: absolute; left: 32px; top: 74px;
    font-family: "PT Sans", sans-serif; font-weight: 700; font-size: 26px; letter-spacing: 1px;
    color: var(--brand-blue);
  }

  .header-divider { position: absolute; left: 475px; top: 9px; width: 5px; height: 105px; background: var(--divider-grey); }

  .contact { position: absolute; left: 498px; font-family: "PT Sans", sans-serif; font-size: 16px; line-height: 20px; color: var(--contact-grey); }
  .contact-icon { position: absolute; left: 0; top: 0; width: 31px; height: 18px; }
  .contact-text { position: absolute; left: 42px; top: -2px; white-space: nowrap; }
  .contact-phone { top: 17px; }
  .contact-address { top: 42px; }
  .contact-email { top: 85px; }

  .letter {
    position: absolute; left: 241px; top: 220px; width: 680px;
    font-family: "Tinos", serif; font-size: 21.5px; line-height: 24.7px; color: var(--body-ink);
  }
  .letter p { margin: 0; }
  .letter .gap-lg { margin-top: 49px; }
  .letter .gap-sm { margin-top: 25px; }
  .letter .gap-sign { margin-top: 50px; }

  .footer-wave { position: absolute; left: 190px; top: 730px; width: 740px; height: 202px; }
  .footer-brand {
    position: absolute; left: 780px; top: 778px;
    font-family: "PT Sans", sans-serif; font-weight: 700; font-size: 30px;
    color: var(--brand-blue);
  }
</style>
</head>
<body>
<div class="canvas">
  <header class="header">
    <div class="header-band"></div>
    <div class="header-accent"></div>
    <div class="header-rule"></div>

    <div class="brand-mark"></div>
    <div class="brand-name">BYTEMILL</div>

    <div class="header-divider"></div>

    <div class="contact contact-phone">
      <svg class="contact-icon" viewBox="0 0 31 18" aria-hidden="true">
        <ellipse cx="15.5" cy="9" rx="15.5" ry="9" fill="var(--brand-blue)"/>
        <path d="M11 5.5c1-1 2-.5 2.5.5l.4 1c.2.6-.2 1-.6 1.3.6 1.3 1.6 2.3 2.9 2.9.3-.4.7-.8 1.3-.6l1 .4c1 .5 1.5 1.5.5 2.5-2.5 1.5-9.5-4.5-8-8z" fill="var(--ink-dark)"/>
      </svg>
      <span class="contact-text">+61 455 21 7390</span>
    </div>

    <div class="contact contact-address">
      <svg class="contact-icon" viewBox="0 0 31 18" aria-hidden="true">
        <ellipse cx="15.5" cy="9" rx="15.5" ry="9" fill="var(--brand-blue)"/>
        <path d="M15.5 3.5a4 4 0 0 1 4 4c0 2.5-4 7-4 7s-4-4.5-4-7a4 4 0 0 1 4-4z" fill="var(--ink-dark)"/>
        <circle cx="15.5" cy="7.5" r="1.5" fill="var(--brand-blue)"/>
      </svg>
      <span class="contact-text">PO Box 214<br>Harbourview SA 5099</span>
    </div>

    <div class="contact contact-email">
      <svg class="contact-icon" viewBox="0 0 31 18" aria-hidden="true">
        <ellipse cx="15.5" cy="9" rx="15.5" ry="9" fill="var(--brand-blue)"/>
        <rect x="10" y="5.5" width="11" height="7.5" fill="var(--ink-dark)"/>
        <path d="M10 5.5l5.5 4 5.5-4" fill="none" stroke="var(--brand-blue)" stroke-width="1"/>
      </svg>
      <span class="contact-text">sam@bytemill.com</span>
    </div>
  </header>

  <main class="letter">
    <p>To,<br>Company ABC<br>Subject,</p>
    <p class="gap-lg">Enter You Text Body HereEnter You Text Body Here Enter You<br>Text Body Here Enter You Text Body Here<br>Enter You Text Body HereEnter You Text Body HereEnter You<br>Text Body HereEnter You Text Body HereEnter You Text Body<br>Here</p>
    <p class="gap-sm">Enter You Text Body HereEnter You Text Body Here</p>
    <p class="gap-sm">Enter You Text Body Here Enter You Text Body Here Enter You<br>Text Body Here<br>Enter You Text Body Here</p>
    <p class="gap-sign">Regards,<br>Bytemill</p>
  </main>

  <svg class="footer-wave" viewBox="0 0 740 202" aria-hidden="true">
    <path d="M8 195 L8 50 C40 5 120 0 220 15 C380 40 560 130 650 140 C700 146 725 130 732 110 L732 195 Z"
          fill="var(--ink-dark)" stroke="var(--wave-blue)" stroke-width="7" stroke-linejoin="round"/>
    <rect x="736" y="100" width="4" height="102" fill="var(--page)"/>
  </svg>
  <div class="footer-brand">Bytemill</div>
</div>
</body>
</html>
```